For Lease sign for Property management company in Kansas City

We need someone to take our information and design a standard for lease sign that we can put in front of each of our buildings. I would love for it to do its job of letting people know there are units available but also be unique somehow. Also the aspect ratio of the design would ideally be 4 wide by 3 tall but we open to other ideas. It will be a larger yard sign.

Target Market(s)

Potential Tenants

Industry/Entity Type

Real Estate Development

Font styles to use
Sans Serif

Requirements
Must have
• Our logo, our website (www.quillstead-properties.com), our phone number (816) 555-2719.
Nice to have
• Some how say "For Lease"
Sign to be 4' wide by 3' tall
If there was a place to put the building name that would be cool but not ne
Should not have
• Nothing that I can think of

```html
<!DOCTYPE html>
<html lang="en">
<head>
<meta charset="utf-8">
<title>Quillstead Properties – For Lease Sign</title>
<link href="https://fonts.googleapis.com/css2?family=Montserrat:wght@500;600;700;800;900&display=swap" rel="stylesheet">
<style>
  :root {
    --backdrop: #5a5a5a;
    --sign-white: #ffffff;
    --brand-red: #bd1e2d;
    --brand-orange: #fbb040;
    --ink: #0a0a0a;
  }
  html, body {
    margin: 0;
    padding: 0;
    width: 1200px;
    height: 1200px;
    overflow: hidden;
    background: var(--backdrop);
    font-family: "Montserrat", sans-serif;
  }
  .sign {
    position: absolute;
    left: 0;
    top: 150px;
    width: 1200px;
    height: 899px;
    background: var(--sign-white);
    overflow: hidden;
  }
  .sign-shapes {
    position: absolute;
    inset: 0;
    width: 100%;
    height: 100%;
  }
  .brand {
    position: absolute;
    left: 253px;
    top: 45px;
    display: flex;
    align-items: center;
    gap: 38px;
  }
  .brand-dot {
    width: 198px;
    height: 198px;
    border-radius: 50%;
    background: var(--brand-orange);
    flex: none;
  }
  .brand-name {
    margin: 0;
    color: var(--brand-red);
    font-weight: 800;
    line-height: 1.05;
    font-size: 64px;
    letter-spacing: 1px;
  }
  .brand-name span {
    display: block;
    font-size: 47px;
    letter-spacing: 8.5px;
  }
  .headline {
    position: absolute;
    left: 0;
    right: 0;
    top: 340px;
    margin: 0;
    text-align: center;
    color: var(--sign-white);
    font-weight: 900;
    font-size: 160px;
    line-height: 1;
    letter-spacing: 2px;
    text-shadow: 5px 5px 0 var(--ink);
  }
  .building-name {
    position: absolute;
    left: 100px;
    top: 528px;
    width: 1000px;
    height: 90px;
    box-sizing: border-box;
    background: var(--sign-white);
    border: 1.5px solid var(--brand-orange);
    border-radius: 4px;
    display: flex;
    align-items: center;
    justify-content: center;
    color: var(--ink);
    font-weight: 800;
    font-size: 52px;
    letter-spacing: 1.5px;
  }
  .phone {
    position: absolute;
    left: 167px;
    top: 660px;
    display: flex;
    align-items: center;
    gap: 26px;
  }
  .phone-icon {
    width: 100px;
    height: 100px;
    flex: none;
  }
  .phone-number {
    color: var(--brand-red);
    font-weight: 700;
    font-size: 104px;
    line-height: 1;
    letter-spacing: 1px;
  }
  .website {
    position: absolute;
    left: 0;
    right: 0;
    top: 790px;
    margin: 0;
    text-align: center;
    color: var(--ink);
    font-weight: 600;
    font-size: 60px;
    line-height: 1;
  }
  .website .domain {
    color: var(--brand-orange);
    font-weight: 600;
  }
</style>
</head>
<body>
  <main class="sign">
    <svg class="sign-shapes" viewBox="0 0 1200 899" preserveAspectRatio="none" aria-hidden="true">
      <path class="red-band" fill="#bd1e2d"
            d="M0 235 Q600 405 1200 235 L1200 676 Q600 480 0 676 Z"/>
      <path class="orange-rule" fill="none" stroke="#fbb040" stroke-width="8"
            d="M0 222 Q600 402 1200 222"/>
    </svg>

    <header class="brand">
      <div class="brand-dot"></div>
      <h1 class="brand-name">QUILLSTEAD<span>PROPERTIES</span></h1>
    </header>

    <h2 class="headline">FOR LEASE</h2>

    <div class="building-name">BUILDING NAME HERE</div>

    <div class="phone">
      <svg class="phone-icon" viewBox="0 0 100 100" aria-hidden="true">
        <circle cx="50" cy="50" r="46" fill="#bd1e2d" stroke="#fbb040" stroke-width="7"/>
        <path fill="#fbb040"
              d="M33 26c3-2 6-1 7 2l5 9c1 2 0 4-2 5l-3 2c2 6 7 12 13 15l2-3c1-2 3-3 5-2l9 5c3 1 3 4 1 7l-3 4c-3 3-8 3-13 1-14-6-25-18-30-32-2-5 0-10 4-13z"/>
      </svg>
      <span class="phone-number">(816) 555-2719</span>
    </div>

    <p class="website">www.<span class="domain">Quillstead-Properties</span>.com</p>
  </main>
</body>
</html>
```